Tallowmere Capital Partners- Business Card

We need a professional business card that conveys confidence and trust. Strength. A modern and still yet, traditional financial planner/advisor format. I will upload a logo file or two, you do not have to use it, if it does not work for the design.

Target Market(s)

high net worth

Industry/Entity Type

Finance

Contact Information for Business Card

Address: 24836 Orchard Ave. Suite 400, Huntington Beach, CA 93518, website: tallowmerecap.example, ph # (555) 271-6094, email address: rpoulsen@tallowmerecap.example

```html
<!DOCTYPE html>
<html lang="en">
<head>
<meta charset="utf-8">
<title>Tallowmere Capital Partners – Business Card</title>
<link href="https://fonts.googleapis.com/css2?family=Playfair+Display:wght@500&family=Montserrat:wght@700&family=Roboto:wght@400&display=swap" rel="stylesheet">
<style>
  :root {
    --backdrop: #2b2b2d;
    --card-blue: #1f2f8f;
    --card-blue-deep: #16226e;
    --gold: #c9a13f;
    --white: #f4f5fa;
    --muted: #b9c0e6;
    --divider: rgba(255,255,255,0.35);
  }
  * { margin: 0; padding: 0; box-sizing: border-box; }
  html, body { width: 1200px; height: 900px; overflow: hidden; }
  body {
    background: radial-gradient(circle at 50% 40%, #3a3a3d, var(--backdrop) 75%);
    display: flex; align-items: center; justify-content: center; gap: 70px;
    font-family: "Roboto", sans-serif;
  }
  .card {
    background: linear-gradient(160deg, var(--card-blue), var(--card-blue-deep));
    border-radius: 18px;
    box-shadow: 0 20px 40px rgba(0,0,0,0.45);
    position: relative;
  }
  /* Back side */
  .card-back {
    width: 320px; height: 560px;
    display: flex; align-items: center; justify-content: center;
    overflow: hidden;
  }
  .card-back .pattern-field {
    position: absolute; inset: 0;
    background: radial-gradient(circle at 50% 60%, #2a3ba3, var(--card-blue-deep) 80%);
  }
  .card-back .brand-name {
    position: relative; top: 60px;
    font-family: "Playfair Display", serif; font-weight: 500;
    color: var(--gold); font-size: 17px; letter-spacing: 1.5px;
    text-transform: uppercase; text-align: center; line-height: 1.5;
    display: flex; flex-direction: column; align-items: center; gap: 12px;
  }
  .brand-square { width: 18px; height: 18px; border: 2px solid var(--gold); }
  /* Front side */
  .card-front { width: 620px; height: 360px; padding: 46px 44px; }
  .front-brand {
    display: flex; align-items: center; gap: 14px;
    font-family: "Playfair Display", serif; font-weight: 500;
    color: var(--gold); font-size: 25px; letter-spacing: 1px; text-transform: uppercase;
    white-space: nowrap;
  }
  .front-brand .brand-square { width: 26px; height: 26px; }
  .details { display: flex; margin-top: 52px; align-items: stretch; }
  .person { text-align: right; padding-right: 22px; border-right: 1px solid var(--divider); min-width: 200px; }
  .person-name { font-family: "Montserrat", sans-serif; font-weight: 700; color: var(--gold); font-size: 20px; text-transform: uppercase; white-space: nowrap; }
  .person-title { color: var(--muted); font-size: 13px; margin-top: 4px; }
  .contact { list-style: none; padding-left: 22px; color: var(--white); font-size: 15px; line-height: 1.75; }
  .contact li, .address { display: flex; align-items: center; gap: 9px; white-space: nowrap; }
  .contact svg, .address svg { width: 13px; height: 13px; fill: var(--gold); flex: none; }
  .contact .icon-mail { fill: none; stroke: var(--gold); stroke-width: 1.6; }
  .address { color: var(--white); font-size: 15px; margin-top: 26px; }
</style>
</head>
<body>
  <section class="card card-back">
    <div class="pattern-field" role="img" aria-label="Embossed repeating monogram pattern in dark blue with silver foil"></div>
    <div class="brand-name"><span class="brand-square"></span>Tallowmere<br>Capital Partners</div>
  </section>

  <section class="card card-front">
    <div class="front-brand"><span class="brand-square"></span>Tallowmere Capital Partners</div>
    <div class="details">
      <div class="person">
        <div class="person-name">Rhea Poulsen</div>
        <div class="person-title">Founder &amp; CEO</div>
      </div>
      <ul class="contact">
        <li><svg viewBox="0 0 16 16"><path d="M3 1h3l1.5 4-2 1.2a9 9 0 0 0 4.3 4.3L11 8.5l4 1.5v3a2 2 0 0 1-2 2A12 12 0 0 1 1 3a2 2 0 0 1 2-2z"/></svg>(555) 271-6094</li>
        <li><svg class="icon-mail" viewBox="0 0 16 16"><path d="M1.5 3.5h13v9h-13z M1.5 3.5l6.5 5.5 6.5-5.5"/></svg>rpoulsen@tallowmerecap.example</li>
        <li><svg viewBox="0 0 16 16"><circle cx="8" cy="8" r="7"/></svg>www.tallowmerecap.example</li>
      </ul>
    </div>
    <div class="address"><svg viewBox="0 0 16 16"><path d="M8 0a5.5 5.5 0 0 0-5.5 5.5C2.5 10 8 16 8 16s5.5-6 5.5-10.5A5.5 5.5 0 0 0 8 0zm0 7.5a2 2 0 1 1 0-4 2 2 0 0 1 0 4z"/></svg>24836 Orchard Ave. Suite 400, Huntington Beach, CA 93518</div>
  </section>
</body>
</html>
```